Commercial Construction Company

We need a business card design based on our current logo. We are a commercial general contractor based in Southern California that specializes in bank remodels. We would like to see designs that incorporate dark blue. The final design should portray an image of professionalism and quality.

If possible, I would like to add metallic foil to the design. Thank you

```html
<!DOCTYPE html>
<html lang="en">
<head>
<meta charset="UTF-8">
<title>Kestrel Commercial Builders – Business Card</title>
<link href="https://fonts.googleapis.com/css2?family=Raleway:wght@400;500;600;700&display=swap" rel="stylesheet">
<style>
  :root {
    --backdrop: #c9cacc;
    --navy: #1b2a52;
    --gold: #d1a63c;
    --white: #ffffff;
    --brand-blue: #1d4a8c;
    --ink: #161a24;
    --muted: #8c8f96;
    --edge-blue: #a9d3ee;
  }
  * { margin: 0; padding: 0; box-sizing: border-box; }
  html, body {
    width: 1200px; height: 913px; overflow: hidden;
    background: var(--backdrop);
    font-family: 'Raleway', sans-serif;
  }
  .stage { position: relative; width: 1200px; height: 913px; }

  .card {
    position: absolute;
    width: 560px; height: 320px;
    border-radius: 18px;
    overflow: hidden;
  }

  /* Front */
  .card--front {
    left: 70px; top: 120px;
    background: var(--navy);
    box-shadow: 0 6px 0 #14203f, 0 14px 28px rgba(0,0,0,.25);
    display: flex; align-items: center; justify-content: center;
  }
  .front-brand {
    display: flex; align-items: center; gap: 16px;
    color: var(--gold);
    font-weight: 700; font-size: 27px; letter-spacing: .5px;
    line-height: 1.15;
  }
  .front-brand .brand-dot {
    width: 52px; height: 52px; border-radius: 50%;
    background: var(--gold); flex-shrink: 0;
  }

  /* Back */
  .card--back {
    left: 570px; top: 470px;
    background: var(--white);
    box-shadow: 0 6px 0 var(--edge-blue), 0 14px 28px rgba(0,0,0,.2);
    display: flex; align-items: center;
  }
  .back-brand {
    width: 265px;
    display: flex; align-items: center; gap: 12px;
    padding-left: 30px;
    color: var(--ink);
    font-weight: 700; font-size: 19px; line-height: 1.2;
  }
  .back-brand .brand-dot {
    width: 38px; height: 38px; border-radius: 50%;
    background: var(--brand-blue); flex-shrink: 0;
  }
  .divider {
    width: 1.5px; height: 200px;
    background: var(--brand-blue);
    margin-right: 26px;
  }
  .details { color: var(--muted); font-size: 13.5px; line-height: 1.35; }
  .person-name {
    color: var(--brand-blue);
    font-weight: 500; font-size: 22px; letter-spacing: .3px;
  }
  .person-role { font-size: 14px; margin-bottom: 22px; }
  .address { margin-bottom: 18px; }
  .contact-list { list-style: none; }
  .contact-list li { display: flex; align-items: center; gap: 9px; margin-bottom: 3px; }
  .contact-list svg { width: 13px; height: 13px; fill: var(--brand-blue); flex-shrink: 0; }
</style>
</head>
<body>
<main class="stage">

  <section class="card card--front" aria-label="Card front">
    <div class="front-brand">
      <span class="brand-dot"></span>
      <span>Kestrel Commercial<br>Builders</span>
    </div>
  </section>

  <section class="card card--back" aria-label="Card back">
    <div class="back-brand">
      <span class="brand-dot"></span>
      <span>Kestrel Commercial<br>Builders</span>
    </div>
    <div class="divider"></div>
    <div class="details">
      <div class="person-name">DANIEL AVERY</div>
      <div class="person-role">Director</div>
      <p class="address">4120 Harbor View Drive,<br>Suite 310,<br>Ontario, CA 91761</p>
      <ul class="contact-list">
        <li>
          <svg viewBox="0 0 24 24" aria-hidden="true"><path d="M6.6 10.8a15.1 15.1 0 0 0 6.6 6.6l2.2-2.2a1 1 0 0 1 1-.25 11.4 11.4 0 0 0 3.6.57 1 1 0 0 1 1 1V20a1 1 0 0 1-1 1A17 17 0 0 1 3 4a1 1 0 0 1 1-1h3.5a1 1 0 0 1 1 1c0 1.25.2 2.45.57 3.57a1 1 0 0 1-.25 1z"/></svg>
          9095550148
        </li>
        <li>
          <svg viewBox="0 0 24 24" aria-hidden="true"><path d="M2 5h20v14H2z M2 5l10 8 10-8" /></svg>
          info@kestrelcb.com
        </li>
        <li>
          <svg viewBox="0 0 24 24" aria-hidden="true"><circle cx="12" cy="12" r="10"/></svg>
          www.kestrelcb.com
        </li>
      </ul>
    </div>
  </section>

</main>
</body>
</html>
```